velmorino.eu :: Design ideas (no coding) for key pages of Personalized greeting cards online store

We need your vision on modern, clean, easy to read user interface (UI) for online service of personalized printed products, like greeting cards, postcards, fridge magnets, clips and etc.
Your vision should include UI presentation for:
- Home page with login (including soc nets)
- Product Designer page
- Cart pages (products and address selection)
- Example of general internal page (pricing, terms, etc)
- Artist info and portfolio page
We are looking for ideas we will love, NOT complete design of a whole site.
Top design/vision will we used as a basement for separate contract on complete design of the site.

UI should be based on existing functionality with some extent. It should not break ideas or methods used on prototype but designers are free to offer own product presentations, designer’s layout and cart views.

Prototype:
English: http://velmorino.eu
Russian: http://velmorino.ru
Lithuanian: http://velmorino.lt

Target Market(s)

People of 16-45 y.o. who likes to be distinctive, personal.

Industry/Entity Type

Store

Requirements
Must have
• Your work should meet attached requirements.
Site is multilingual. Wording should assume varieties in length on different languages.
Clean and easy to read UI
Flat design preferrably
Should be based on assets which are free or available for royalty-free licensing
Should not have
• heavy, meaningless 3D and shadow effects
Show NOT copy sites like: plonkra.com, tarnwick.co.uk

```html
<!DOCTYPE html>
<html lang="en">
<head>
<meta charset="utf-8">
<title>velmorino – Greeting Cards</title>
<link rel="stylesheet" href="https://fonts.googleapis.com/css2?family=Source+Sans+3:wght@400;600;700&family=PT+Sans+Narrow:wght@400;700&display=swap">
<style>
:root{
  --page:#ffffff;
  --side:#fbdfe0;
  --main:#fde5d5;
  --brand:#9b2a1c;
  --nav:#b5473a;
  --active:#f2a096;
  --teal:#2a8d85;
  --navy:#33607f;
  --orange:#f97a25;
  --meta:#8d8d8d;
  --price:#a0241a;
  --white:#ffffff;
}
*{box-sizing:border-box;margin:0;padding:0}
html,body{width:1155px;height:1200px;overflow:hidden;background:var(--page);font-family:"Source Sans 3",sans-serif}
.canvas{position:relative;width:1155px;height:1200px}

.sidebar{position:absolute;left:45px;top:234px;width:150px;height:768px;background:var(--side);box-shadow:0 2px 6px rgba(0,0,0,.12)}
.brand{position:absolute;top:100px;left:0;width:150px;text-align:center;color:var(--brand);font-size:22px;font-weight:400;letter-spacing:.5px}
.brand-dot{display:inline-block;width:8px;height:8px;border-radius:50%;background:var(--brand);margin-right:6px;vertical-align:middle}
.sub-nav{position:absolute;top:152px;left:15px;width:122px;list-style:none}
.sub-nav li{display:flex;justify-content:space-between;align-items:center;color:var(--nav);font-weight:700;font-size:17px;height:26px}
.sub-nav .dot{width:11px;height:11px;border-radius:50%;border:2.5px solid var(--brand)}
.sub-nav .dot.filled{background:var(--brand)}
.media{position:absolute;left:0;width:150px;text-align:center;font-weight:700;font-size:17px}
.media svg{display:block;margin:0 auto 6px}
.media.active{top:230px;height:100px;background:var(--active);color:var(--white);padding-top:8px;text-shadow:0 1px 2px rgba(0,0,0,.25)}
.media.greeting{top:362px;color:var(--teal)}
.media.postcards{top:484px;color:var(--navy)}
.media.square{top:608px;color:var(--orange)}
.copyright{position:absolute;bottom:16px;width:150px;text-align:center;font-size:11px;color:var(--brand)}

.colour-strip{position:absolute;left:195px;top:234px;width:20px;height:768px;display:flex;flex-direction:column}
.colour-strip span{display:block;height:38.5px}
.colour-strip .mix{flex:1;background:repeating-linear-gradient(90deg,#c5242c 0 5px,#1f88c6 5px 10px,#e2497f 10px 15px,#3c3c55 15px 20px)}

.main{position:absolute;left:215px;top:234px;width:854px;height:768px;background:var(--main)}
.banner{position:absolute;left:35px;top:0;width:819px;height:80px;background:linear-gradient(100deg,#e6665a 0%,#f2b07a 18%,#2f8c8a 36%,#d2685c 52%,#2e5575 68%,#e7b07e 80%,#355b7a 100%);box-shadow:0 3px 5px rgba(0,0,0,.2)}
.tagline{position:absolute;left:16px;top:12px;color:var(--white);font-weight:700;font-size:23px;line-height:29px;text-shadow:1px 1px 2px rgba(0,0,0,.55)}
.account{position:absolute;right:16px;top:30px;display:flex;align-items:center;color:var(--white);font-weight:700;font-size:14px;text-shadow:1px 1px 2px rgba(0,0,0,.5)}
.account .sep{width:2px;height:20px;background:var(--white);margin:0 15px 0 20px}

.card{position:absolute;top:180px;width:180px;background:var(--white);box-shadow:0 1px 4px rgba(0,0,0,.15)}
.card .art{display:block;width:180px}
.card .meta{padding:10px 8px 0;font-size:11.5px;line-height:14.5px;color:var(--meta);height:62px}
.card .foot{display:flex;justify-content:space-between;align-items:center;padding:0 10px 8px 8px}
.card .price{font-family:"PT Sans Narrow",sans-serif;font-size:20px;color:var(--price)}
.card .bar{height:6px;background:linear-gradient(90deg,#e8d8a8 0 7%,#c8c8c8 7% 11%,#8a8a8a 11% 15%,#f4a8c0 15% 20%,#a8b8dc 20% 25%,#8a5a2a 25% 30%,#5fbf3a 30% 35%,#3c3c55 35% 40%,#2e6a1a 40% 45%,#c5242c 45% 50%,#4ec3c0 50% 55%,#c96a3a 55% 60%,#f08c1e 60% 65%,#1e6ec0 65% 70%,#f5b91e 70% 75%,#e2497f 75% 80%,#3b3b8f 80% 85%,#1f88c6 85% 90%,#6a9a1f 90% 100%)}
.c1{left:35px}.c2{left:236px}.c3{left:438px}.c4{left:639px}
.c1 .art{height:183px;background:linear-gradient(135deg,#1d3fc8,#e2602a 50%,#1d3fc8)}
.c2 .art{height:274px;background:linear-gradient(160deg,#dfe6f2,#f6efe0 50%,#b8cbe6)}
.c3 .art{height:266px;background:radial-gradient(circle at 50% 45%,#f3efe0 0 22%,#3f7a2e 30%,#c8241f 48%)}
.c4 .art{height:266px;background:linear-gradient(120deg,#2b4d8c,#b48a4a 45%,#c23a2a 70%,#6a4a2a)}
</style>
</head>
<body>
<div class="canvas">

  <aside class="sidebar">
    <div class="brand"><span class="brand-dot"></span>velmorino</div>
    <ul class="sub-nav">
      <li>Products <span class="dot"></span></li>
      <li>Artist <span class="dot filled"></span></li>
    </ul>
    <div class="media active">
      <svg width="36" height="52" viewBox="0 0 36 52" fill="none" stroke="#fff" stroke-width="4">
        <path d="M8 2 L24 36 M28 2 L12 36"/>
        <circle cx="10" cy="43" r="6"/><circle cx="26" cy="43" r="6"/>
      </svg>
      All Medias
    </div>
    <div class="media greeting">
      <svg width="46" height="52" viewBox="0 0 46 52"><rect x="2" y="2" width="28" height="44" fill="var(--teal)"/><rect x="14" y="26" width="30" height="22" fill="var(--teal)" stroke="var(--side)" stroke-width="2"/></svg>
      Greeting Cards
    </div>
    <div class="media postcards">
      <svg width="46" height="52" viewBox="0 0 46 52"><rect x="2" y="2" width="32" height="32" fill="var(--navy)"/><rect x="16" y="22" width="28" height="26" fill="var(--navy)" stroke="var(--side)" stroke-width="2"/></svg>
      PostCards
    </div>
    <div class="media square">
      <svg width="46" height="52" viewBox="0 0 46 52"><path d="M2 8 L30 2 L30 6 L44 6 L44 50 L2 50 Z" fill="var(--orange)"/></svg>
      Square Cards
    </div>
    <div class="copyright">© 2014 velmorino</div>
  </aside>

  <div class="colour-strip">
    <span style="background:#6a9a1f"></span><span style="background:#1f88c6"></span><span style="background:#3b3b8f"></span><span style="background:#e2497f"></span><span style="background:#f5b91e"></span><span style="background:#1e6ec0"></span><span style="background:#f08c1e"></span><span style="background:#c96a3a"></span><span style="background:#4ec3c0"></span><span style="background:#c5242c"></span><span style="background:#2e6a1a"></span><span style="background:#3c3c55"></span><span style="background:#5fbf3a"></span><span style="background:#8a5a2a"></span><span style="background:#a8b8dc"></span><span style="background:#f4a8c0"></span><span style="background:#8a8a8a"></span><span style="background:#c8c8c8"></span><span style="background:#e8d8a8"></span><span class="mix"></span>
  </div>

  <main class="main">
    <header class="banner" role="img" aria-label="Colourful triangle pattern banner">
      <div class="tagline">The Individual Greeting Cards<br>According to your mood</div>
      <div class="account"><span>Log In</span><span class="sep"></span><span>Sign Up</span></div>
    </header>

    <article class="card c1">
      <div class="art" role="img" aria-label="Card art: four painted Christmas trees and stars on blue"></div>
      <p class="meta">Loft Print Studio &nbsp;|&nbsp; Vaiva Zvaigzdes Kaledos &nbsp;|&nbsp; Naujieji Metai</p>
      <div class="foot"><svg width="20" height="18" viewBox="0 0 20 18"><path d="M0 7 L10 0 L20 7 V18 H0 Z" fill="#9a9a9a"/></svg><span class="price">€ 2.99</span></div>
      <div class="bar"></div>
    </article>

    <article class="card c2">
      <div class="art" role="img" aria-label="Card art: patchwork with a toy bear"></div>
      <p class="meta">Loft Print Studio &nbsp;|&nbsp; Vaiva Zvaigzdes Kaledos &nbsp;|&nbsp; Naujieji Metai</p>
      <div class="foot"><svg width="20" height="18" viewBox="0 0 20 18"><path d="M0 7 L10 0 L20 7 V18 H0 Z" fill="#9a9a9a"/></svg><span class="price">€ 2.99</span></div>
      <div class="bar"></div>
    </article>

    <article class="card c3">
      <div class="art" role="img" aria-label="Card art: white flowers and pine cones on red"></div>
      <p class="meta">Loft Print Studio &nbsp;|&nbsp; Vaiva Zvaigzdes Kaledos &nbsp;|&nbsp; Naujieji Metai</p>
      <div class="foot"><svg width="20" height="18" viewBox="0 0 20 18"><path d="M0 7 L10 0 L20 7 V18 H0 Z" fill="#9a9a9a"/></svg><span class="price">€ 2.99</span></div>
      <div class="bar"></div>
    </article>

    <article class="card c4">
      <div class="art" role="img" aria-label="Card art: painted nativity scene in a stable"></div>
      <p class="meta">Loft Print Studio &nbsp;|&nbsp; Vaiva Zvaigzdes Kaledos &nbsp;|&nbsp; Naujieji Metai</p>
      <div class="foot"><svg width="20" height="18" viewBox="0 0 20 18"><rect x="1" y="1" width="17" height="17" fill="var(--brand)"/></svg><span class="price">€ 2.99</span></div>
      <div class="bar"></div>
    </article>
  </main>

</div>
</body>
</html>
```